Postcard and Door Hanger Design

We need two pieces designed for marketing. Both will use the same logo and photo just the text will be slightly different. We need these designs looking very modern, clean, and simple while having the important information to stand out.

Postcard: 2 sided
- Side 1 just have large logo with our website and phone number
- Side 2 below.
- 4 x 6
- Use photo of house provided
- "Going Above and Beyond Every Time"
- "Call TODAY to Reserve your project by May 1st and receive 10% off"
- "Residential and Commercial"
- Our contact is 555-284-7190
- Website is www.brightoakcoatings.example
- Might include something like "check out our portfolio on our website"

Use the above as a guidline and be creative with it, add or take away as you see fit as we are open to suggestions.

Door Hanger: 2 sided
Side 1 - Logo with contact details
Side 2 - Below
- 4 x 11
- "We are painting your neighborhood"
-"come see us in action at (then leave a space where we can stick a label onto our door hanger with an address of a home we are painting)
- Call today for a FREE ESTIMATE
- 555-284-7190
- www.brightoakcoatings.example

https://files.example.net/sh/q3rt91xk2mzb5ap/TL8PLWQ-ZR

https://files.example.net/sh/vb62ytn0rwc37jd/KUgHHSwnTx

https://files.example.net/sh/p4z19fdh6wq3nn5/rxs-aB7KLe

```html
<!DOCTYPE html>
<html lang="en">
<head>
<meta charset="utf-8">
<title>BrightOak Coatings Postcard</title>
<link rel="stylesheet" href="https://fonts.googleapis.com/css2?family=Libre+Baskerville:wght@400;700&family=Playfair+Display:wght@600;700&family=Raleway:wght@400;500&display=swap">
<style>
  :root {
    --slate: #44525c;
    --teal: #17bdb9;
    --band-grey: #a9aeb3;
    --white: #ffffff;
    --page: #ffffff;
    --label: #4a4a4a;
    --ink: #3a3f44;
    --sky: #8fb3d6;
    --garden: #5f7a3f;
    --interior: #6b5444;
  }
  * { box-sizing: border-box; margin: 0; padding: 0; }
  html, body { width: 1200px; height: 848px; overflow: hidden; background: var(--page); }
  .canvas { position: relative; width: 1200px; height: 848px; }

  .sheet-label {
    position: absolute; left: 876px; top: 40px; width: 324px; height: 47px;
    background: var(--label); color: var(--white);
    font: 400 21px/47px "Libre Baskerville", serif; padding-left: 48px;
  }

  .card { position: absolute; background: var(--slate); overflow: hidden; }
  .card-front { left: 84px; top: 199px; width: 527px; height: 351px; }
  .card-back { left: 640px; top: 199px; width: 533px; height: 354px; }
  .teal-strip { position: absolute; left: 0; top: 0; width: 49px; height: 100%; background: var(--teal); }

  /* Front */
  .brand-mark { position: absolute; left: 279px; top: 91px; width: 18px; height: 18px; background: var(--teal); }
  .brand-name {
    position: absolute; left: 49px; right: 0; top: 120px; text-align: center;
    font: 400 21px/1.2 "Raleway", sans-serif; letter-spacing: 3px; color: var(--white);
  }
  .front-band {
    position: absolute; left: 49px; right: 0; top: 193px; height: 35px;
    background: var(--white); border-top: 6px solid var(--band-grey); border-bottom: 5px solid var(--band-grey);
  }
  .front-url {
    position: absolute; left: 49px; right: 0; top: 204px; text-align: center;
    font: 400 13px/1 "Libre Baskerville", serif; letter-spacing: 1.2px; color: var(--ink);
  }
  .front-phone {
    position: absolute; left: 49px; right: 0; top: 233px; text-align: center;
    font: 400 15px/1 "Libre Baskerville", serif; letter-spacing: 1px; color: var(--white);
  }
  .phone-icon { display: inline-block; width: 14px; height: 12px; vertical-align: -1px; margin-right: 3px; }

  /* Back */
  .vertical-url {
    position: absolute; left: 0; top: 0; width: 49px; height: 100%;
    display: flex; align-items: center; justify-content: center;
  }
  .vertical-url span {
    writing-mode: vertical-rl; transform: rotate(180deg); white-space: nowrap;
    font: 400 11px/1 "Libre Baskerville", serif; letter-spacing: 1.2px; color: var(--white);
  }
  .photo-house {
    position: absolute; left: 49px; top: 0; width: 261px; height: 172px;
    background: linear-gradient(180deg, var(--sky) 0%, #b6c9d8 28%, #6f7476 45%, var(--garden) 70%, #4b6132 100%);
  }
  .photo-interior {
    position: absolute; left: 304px; top: 199px; width: 229px; height: 155px;
    background: linear-gradient(160deg, #8a7a6a 0%, var(--interior) 45%, #3d302a 100%);
  }
  .headline-panel { position: absolute; left: 310px; top: 0; width: 223px; height: 172px; text-align: center; color: var(--white); }
  .panel-mark { display: inline-block; width: 10px; height: 10px; background: var(--teal); margin-top: 16px; }
  .panel-brand { font: 400 9px/1.2 "Raleway", sans-serif; letter-spacing: 1.5px; margin-top: 4px; }
  .service-title { font: 700 20px/1.2 "Playfair Display", serif; letter-spacing: 1.5px; }
  .service-title.first { margin-top: 8px; }
  .service-amp { font: 600 26px/1 "Playfair Display", serif; }
  .tagline { font: 700 8.5px/1 "Libre Baskerville", serif; margin-top: 8px; }

  .offer-band {
    position: absolute; left: 49px; right: 0; top: 172px; height: 27px;
    background: var(--white); border-top: 6px solid var(--band-grey);
  }
  .offer-line, .offer-receive, .offer-discount, .offer-rule { z-index: 2; }
  .offer-line {
    position: absolute; left: 67px; top: 180px; white-space: nowrap;
    font: 700 13.5px/1 "Libre Baskerville", serif; color: var(--ink); letter-spacing: .3px;
  }
  .offer-receive {
    position: absolute; left: 67px; top: 202px;
    font: 700 11px/1 "Libre Baskerville", serif; color: var(--white);
  }
  .offer-discount {
    position: absolute; left: 156px; top: 200px; white-space: nowrap;
    font: 700 30px/1 "Playfair Display", serif; color: var(--white); letter-spacing: 1px;
  }
  .offer-rule { position: absolute; left: 156px; top: 233px; width: 128px; height: 1px; background: var(--white); }
  .back-phone {
    position: absolute; left: 86px; top: 266px;
    font: 700 19px/1 "Libre Baskerville", serif; color: var(--white); letter-spacing: .5px;
  }
  .back-phone .phone-icon { width: 24px; height: 18px; vertical-align: -2px; margin-right: 6px; }
  .estimate-note {
    position: absolute; left: 89px; top: 291px;
    font: 700 9px/1 "Libre Baskerville", serif; color: var(--white);
  }
</style>
</head>
<body>
<div class="canvas">
  <div class="sheet-label">BRIGHTOAK Postcard</div>

  <section class="card card-front">
    <div class="teal-strip"></div>
    <span class="brand-mark"></span>
    <div class="brand-name">BRIGHTOAK COATINGS</div>
    <div class="front-band"></div>
    <div class="front-url">WWW.BRIGHTOAKCOATINGS.EXAMPLE</div>
    <div class="front-phone">
      <svg class="phone-icon" viewBox="0 0 24 18" aria-hidden="true"><path d="M2 7c0-4 20-4 20 0v2h-5V6H7v3H2z M6 10h12l3 7H3z" fill="currentColor"/><circle cx="12" cy="13.5" r="2" fill="#44525c"/></svg>555-284-7190
    </div>
  </section>

  <section class="card card-back">
    <div class="teal-strip"></div>
    <div class="vertical-url"><span>WWW.BRIGHTOAKCOATINGS.EXAMPLE</span></div>
    <div class="photo-house" role="img" aria-label="Photo of a grey two-storey house with landscaped garden"></div>
    <div class="headline-panel">
      <span class="panel-mark"></span>
      <div class="panel-brand">BRIGHTOAK COATINGS</div>
      <div class="service-title first">Residential</div>
      <div class="service-amp">&amp;</div>
      <div class="service-title">Commercial</div>
      <div class="tagline">Going Above and Beyond Every Time</div>
    </div>
    <div class="offer-band"></div>
    <div class="photo-interior" role="img" aria-label="Photo of a modern kitchen interior with island and bar stools"></div>
    <div class="offer-line">Call TODAY to Reserve your project by May 1st</div>
    <div class="offer-receive">and receive</div>
    <div class="offer-discount">10% off</div>
    <div class="offer-rule"></div>
    <div class="back-phone">
      <svg class="phone-icon" viewBox="0 0 24 18" aria-hidden="true"><path d="M2 7c0-4 20-4 20 0v2h-5V6H7v3H2z M6 10h12l3 7H3z" fill="currentColor"/><circle cx="12" cy="13.5" r="2" fill="#44525c"/></svg>555-284-7190
    </div>
    <div class="estimate-note">Call for a FREE ESTIMATE quote</div>
  </section>
</div>
</body>
</html>
```